Rally 84 Training is our company name. and instruction

We provide emergency medical training for CPR (Cardiopulmonary Resuscitation) /AED (Automated External Defibrillation) , BLS (Basic Life Support, First Aid, Bloodborne Pathogens
We travel to the client, give certified (CVL) Continental Vitality League (CVL) instruction for job/industry certification in the areas listed.
CVL Kin and Neighbors noncertified instruction

Target Market(s)

Medical professionals, job required certification

Industry/Entity Type

Medical And Science

Contact Information for Business Card

Logo
Phone, email, address, website address, FB, Instagram

Font styles to use
Serif
Sans Serif

Colors
fff2fe
ff1b2f

Requirements
Must have
• Logo
Course taught: CPR (Cardiopulmonary Resuscitation)
AED (Automated External Defibrillation)
First Aid
BLS (Basic Life Support)
Bloodborne Pathogens
Offsite instruction - we come to you
Nice to have
• Red/Black scheme
Possible ecg/heart rhythm design
Should not have
• Cartoon images

```html
<!DOCTYPE html>
<html lang="en">
<head>
<meta charset="utf-8">
<title>Rally 84 Training – Business Card</title>
<link rel="stylesheet" href="https://fonts.googleapis.com/css2?family=Tinos:wght@400;700&family=Arimo:wght@400;700&display=swap">
<style>
  :root {
    --stage: #2a2a2c;
    --card-dark: #1c1b20;
    --card-light: #ffffff;
    --brand-red: #e61e2a;
    --gold: #d8aa2e;
    --ink: #1a1a1a;
    --muted-light: #c9c9cc;
    --rule: #ececec;
  }
  * { box-sizing: border-box; margin: 0; padding: 0; }
  html, body { width: 1200px; height: 900px; overflow: hidden; }
  body {
    background: var(--stage);
    font-family: "Arimo", Arial, sans-serif;
    position: relative;
  }
  .card {
    position: absolute;
    width: 560px;
    height: 320px;
    border-radius: 3px;
    box-shadow: 0 10px 30px rgba(0,0,0,0.45);
    overflow: hidden;
  }

  /* Back side */
  .card--back { left: 320px; top: 100px; background: var(--card-dark); }
  .back-brand {
    position: absolute; top: 30px; right: 34px;
    display: flex; align-items: center; gap: 14px;
  }
  .brand-dot {
    width: 78px; height: 78px; border-radius: 50%;
    background: var(--brand-red);
    border: 4px solid #d9d9d9;
  }
  .back-brand .brand-name {
    font-family: "Tinos", "Times New Roman", serif;
    font-weight: 700; font-size: 22px; color: var(--gold);
  }
  .social {
    position: absolute; top: 140px; right: 40px;
    display: flex; gap: 6px;
  }
  .social span {
    width: 20px; height: 20px; border-radius: 50%;
    border: 1.5px solid #e6e6e6;
  }
  .courses { position: absolute; left: 40px; bottom: 34px; }
  .courses h2 {
    font-family: "Tinos", "Times New Roman", serif;
    font-weight: 700; font-size: 19px; color: var(--gold);
    letter-spacing: 0.5px; margin-bottom: 10px;
  }
  .courses ul { list-style: none; }
  .courses li {
    color: var(--muted-light); font-size: 15px; line-height: 21px;
    display: flex; align-items: center; gap: 8px;
  }
  .courses li::before {
    content: ""; width: 8px; height: 8px; border-radius: 50%;
    background: var(--brand-red); flex: none;
  }

  /* Front side */
  .card--front { left: 320px; top: 480px; background: var(--card-light); display: flex; }
  .front-brand {
    width: 50%; display: flex; flex-direction: column;
    align-items: center; justify-content: center; gap: 16px;
    border-right: 1px solid var(--rule);
  }
  .front-brand .brand-dot { width: 130px; height: 130px; border: 5px solid #222; }
  .front-brand .brand-name {
    font-family: "Tinos", "Times New Roman", serif;
    font-weight: 700; font-size: 28px; color: var(--brand-red);
  }
  .contact { width: 50%; padding: 74px 0 0 34px; color: var(--ink); }
  .contact .person {
    font-family: "Tinos", "Times New Roman", serif;
    font-weight: 700; font-size: 23px; color: var(--brand-red);
    letter-spacing: 0.5px; line-height: 1;
  }
  .contact .role { font-size: 15px; margin: 3px 0 14px; }
  .contact-row { display: flex; align-items: center; gap: 7px; font-size: 15px; line-height: 22px; }
  .contact-row svg { width: 14px; height: 14px; flex: none; }
  .contact-row .web { color: var(--gold); }
  .contact-row .web b { color: var(--brand-red); font-weight: 400; }
  .address { font-size: 15px; line-height: 19px; margin-top: 12px; }
</style>
</head>
<body>

<section class="card card--back" aria-label="Card back">
  <div class="back-brand">
    <span class="brand-name">Rally 84 Training</span>
    <span class="brand-dot"></span>
  </div>
  <div class="social" aria-label="Social profiles"><span></span><span></span></div>
  <div class="courses">
    <h2>COURSE TAUGHT</h2>
    <ul>
      <li>CPR (Cardiopulmonary Resuscitation)</li>
      <li>AED (Automated External Defibrillation)</li>
      <li>First Aid | BLS (Basic Life Support)</li>
      <li>Bloodborne Pathogens</li>
      <li>Offsite instruction - we come to you</li>
    </ul>
  </div>
</section>

<section class="card card--front" aria-label="Card front">
  <div class="front-brand">
    <span class="brand-dot"></span>
    <span class="brand-name">Rally 84 Training</span>
  </div>
  <div class="contact">
    <p class="person">MARCUS HALE</p>
    <p class="role">Managing Director</p>
    <p class="contact-row">
      <svg viewBox="0 0 14 14"><rect x="0.8" y="0.8" width="12.4" height="12.4" rx="2" fill="none" stroke="#e61e2a" stroke-width="1.4"/><path d="M4 3.5l1.6 1.6-0.9 1.2a5 5 0 0 0 3 3l1.2-0.9 1.6 1.6-1 1A6.5 6.5 0 0 1 3 4.5z" fill="#e61e2a"/></svg>
      044-210 864 975
    </p>
    <p class="contact-row">
      <svg viewBox="0 0 14 14"><rect x="0.5" y="2.5" width="13" height="9" fill="#e61e2a"/><path d="M0.5 2.5l6.5 5 6.5-5" fill="none" stroke="#fff" stroke-width="1.2"/></svg>
      info@rally84.example
    </p>
    <p class="contact-row">
      <svg viewBox="0 0 14 14"><circle cx="7" cy="7" r="6" fill="none" stroke="#e61e2a" stroke-width="1.4"/><ellipse cx="7" cy="7" rx="2.6" ry="6" fill="none" stroke="#e61e2a" stroke-width="1.2"/><path d="M1 7h12" stroke="#e61e2a" stroke-width="1.2"/></svg>
      <span class="web"><b>www.</b>rally84<b>.example</b></span>
    </p>
    <p class="address">421, Address line goes here<br>45452, Country Name</p>
  </div>
</section>

</body>
</html>
```